Business Card for Wellness Clinic

We need a business card for our new logo. I want it to match the feel of the logo

Target Market(s)

Young professional families looking for holistic health care

Industry/Entity Type

Health And Wellness

Contact Information for Business Card

Our business Name: Brackenfield Health & wellness Centre, our phone #, email address...see attached old business card

Font styles to use
Sans Serif

Colors
33b8a4
cee9f5

Requirements
Must have
• my logo and business name
• Font is "Helvetica Neue LT Std 45 Light" and
• Only for "&" using font "Trajan pro bold"
• Use colors in the logo

```html
<!DOCTYPE html>
<html lang="en">
<head>
<meta charset="utf-8">
<title>Brackenfield Health &amp; Wellness Centre – Business Card</title>
<link rel="stylesheet" href="https://fonts.googleapis.com/css2?family=Inter:ital,wght@0,300;1,300&display=swap">
<style>
  :root {
    --teal: #33b8a4;
    --mist: #cee9f5;
    --grey-text: #8e9194;
    --grey-rule: #c9cbcd;
    --divider: #4a4f54;
    --white: #ffffff;
  }
  * { margin: 0; padding: 0; box-sizing: border-box; }
  html, body { width: 955px; height: 1200px; overflow: hidden; background: var(--white); }
  body { font-family: "Inter", "Helvetica Neue", Arial, sans-serif; font-weight: 300; color: var(--grey-text); }
  .canvas { position: relative; width: 955px; height: 1200px; }

  /* Front side */
  .card-front { position: absolute; left: 0; top: 0; width: 955px; height: 594px; background: var(--white); overflow: hidden; }
  .brand-panel { position: absolute; left: 0; top: 0; width: 320px; height: 594px; background: var(--teal);
    display: flex; flex-direction: column; align-items: center; justify-content: center; gap: 22px; }
  .brand-panel .brand-square { width: 84px; height: 84px; background: var(--white); border-radius: 10px; }
  .brand-panel .brand-name { color: var(--white); font-size: 22px; line-height: 1.35; text-align: center; letter-spacing: 0.08em; }

  .header-name { position: absolute; left: 320px; top: 0; width: 635px; height: 146px;
    display: flex; flex-direction: column; align-items: center; justify-content: center; gap: 10px; color: var(--grey-text); }
  .header-name .line-one { font-size: 32px; letter-spacing: 0.2em; white-space: nowrap; }
  .header-name .line-two { font-size: 20px; letter-spacing: 0.5em; white-space: nowrap; }
  .header-band { position: absolute; left: 320px; top: 146px; width: 635px; height: 10px; background: var(--teal); }

  .contact { position: absolute; left: 378px; font-size: 27px; line-height: 1; white-space: nowrap; }
  .contact.accent { color: var(--teal); font-style: italic; }
  .doctor-name { top: 183px; }
  .doctor-title { top: 216px; }
  .street { top: 322px; }
  .city { top: 360px; }
  .phone { top: 398px; }
  .website { top: 497px; }
  .email { top: 535px; }

  .side-divider { position: absolute; left: 0; top: 594px; width: 955px; height: 8px; background: var(--divider); }

  /* Back side */
  .card-back { position: absolute; left: 0; top: 602px; width: 955px; height: 598px; background: var(--white); }
  .back-brand { position: absolute; left: 0; top: 70px; width: 955px; display: flex; flex-direction: column; align-items: center; }
  .back-brand .brand-square { width: 120px; height: 120px; background: var(--teal); border-radius: 14px; margin-bottom: 44px; }
  .back-brand .line-one { font-size: 40px; letter-spacing: 0.2em; white-space: nowrap; color: var(--grey-text); }
  .back-brand .line-two { font-size: 24px; letter-spacing: 0.5em; white-space: nowrap; color: var(--grey-text); margin-top: 16px; }

  .appointment-field { position: absolute; font-size: 30px; color: var(--grey-rule); white-space: nowrap; line-height: 1; }
  .field-rule { position: absolute; height: 2px; background: var(--grey-rule); }
  .date-slash { position: absolute; font-size: 30px; color: var(--grey-text); line-height: 1; }
</style>
</head>
<body>
<main class="canvas">
  <section class="card-front" aria-label="Business card front">
    <div class="brand-panel">
      <div class="brand-square"></div>
      <p class="brand-name">Brackenfield<br>Health &amp; Wellness<br>Centre</p>
    </div>
    <header class="header-name">
      <p class="line-one">BRACKENFIELD HEALTH</p>
      <p class="line-two">&amp; WELLNESS CENTRE</p>
    </header>
    <div class="header-band"></div>

    <p class="contact doctor-name">Dr. Maren Holt, N.D.</p>
    <p class="contact accent doctor-title">Naturopathic Doctor</p>
    <p class="contact street">48 Alder Row, Suite 305</p>
    <p class="contact city">Kingsford, ON K7L 2B9</p>
    <p class="contact accent phone">613-555-0142</p>
    <p class="contact website">www.kingsfordnaturopathic.ca</p>
    <p class="contact accent email">mholt@kingsfordnaturopathic.ca</p>
  </section>

  <div class="side-divider"></div>

  <section class="card-back" aria-label="Appointment card back">
    <div class="back-brand">
      <div class="brand-square"></div>
      <p class="line-one">BRACKENFIELD HEALTH</p>
      <p class="line-two">&amp; WELLNESS CENTRE</p>
    </div>

    <p class="appointment-field" style="left:126px; top:444px;">Name:</p>
    <div class="field-rule" style="left:240px; top:472px; width:594px;"></div>

    <p class="appointment-field" style="left:126px; top:510px;">Time:</p>
    <div class="field-rule" style="left:240px; top:538px; width:180px;"></div>

    <p class="appointment-field" style="left:524px; top:510px;">Date:</p>
    <div class="field-rule" style="left:648px; top:538px; width:186px;"></div>
    <span class="date-slash" style="left:698px; top:508px;">/</span>
    <span class="date-slash" style="left:762px; top:508px;">/</span>
  </section>
</main>
</body>
</html>
```